R.T.Pell Logging Web design

Our website needs a redesign. We want it to appear professional and easy to navigate. We will be adding videos and pictures to the new website. We do not sell any products on our website. It should be designed for informational purposes. Our company performs timber harvesting and forest management services. Attached is our new company logo.

www.rtpelllogging-example.com if you want to see our current website.

Industry/Entity Type

Graphic Design

Coding

Coded - Design and coding required

```html
<!DOCTYPE html>
<html lang="en">
<head>
<meta charset="utf-8">
<title>R.T.Pell Logging Company</title>
<link rel="stylesheet" href="https://fonts.googleapis.com/css2?family=Oswald:wght@500&family=Archivo+Narrow:wght@400;600&family=Arimo:ital,wght@0,700;1,400&display=swap">
<style>
  :root {
    --nav-dark: #0a6cbf;
    --nav-light: #00aeef;
    --heading-blue: #1a72b8;
    --text: #111111;
    --rule: #bdbdbd;
    --form-bg: #e9e9e9;
    --field-border: #b5b5b5;
    --button-blue: #0a4fe0;
    --share-grey: #8c9aa8;
    --white: #ffffff;
  }
  * { box-sizing: border-box; margin: 0; padding: 0; }
  html, body { width: 1200px; height: 904px; overflow: hidden; background: var(--white); }
  body { position: relative; font-family: "Archivo Narrow", "Arial Narrow", sans-serif; color: var(--text); }

  .site-name { position: absolute; left: 14px; top: 34px; font-family: "Archivo Narrow", sans-serif;
    font-weight: 600; font-size: 36px; line-height: 1; color: var(--heading-blue); }

  .main-nav { position: absolute; left: 0; top: 105px; width: 1200px; height: 50px;
    background: linear-gradient(90deg, var(--nav-dark) 0%, #0a78cc 35%, var(--nav-light) 70%, var(--nav-light) 100%);
    display: flex; align-items: center; padding-left: 15px; gap: 34px; }
  .main-nav a { font-family: "Oswald", sans-serif; font-weight: 500; font-size: 14px; color: var(--white); text-decoration: none; text-transform: uppercase; }

  .hero { position: absolute; left: 15px; top: 169px; width: 774px; height: 494px; overflow: hidden;
    background:
      radial-gradient(ellipse at 45% 20%, rgba(230,240,220,0.85) 0%, rgba(170,200,150,0.4) 30%, rgba(0,0,0,0) 60%),
      linear-gradient(180deg, #6f8a62 0%, #4d6a3e 40%, #5f8a32 70%, #3f6a22 100%); }
  .hero__label { position: absolute; left: 0; right: 0; top: 273px; text-align: center;
    font-family: "Oswald", sans-serif; font-weight: 500; font-size: 34px; color: var(--white); }
  .hero__arrow { position: absolute; top: 214px; width: 60px; height: 60px; }
  .hero__arrow--prev { left: 44px; }
  .hero__arrow--next { left: 682px; top: 210px; }

  .hero-caption { position: absolute; left: 21px; top: 673px; font-family: "Arimo", Arial, sans-serif;
    font-size: 14px; font-style: italic; line-height: 21px; }

  .welcome { position: absolute; left: 15px; top: 734px; width: 780px; }
  .section-title { font-family: "Oswald", sans-serif; font-weight: 500; font-size: 23px; color: var(--heading-blue); }
  .welcome p { margin-top: 12px; margin-left: 2px; font-size: 17.5px; line-height: 24px; white-space: nowrap; }

  .share { position: absolute; left: 818px; top: 167px; width: 382px; height: 86px;
    border-top: 1px solid var(--rule); border-bottom: 1px solid var(--rule); }
  .share__title { font-family: "Arimo", Arial, sans-serif; font-weight: 700; font-size: 15.5px; margin-top: 6px; word-spacing: 3px; }
  .share__list { display: flex; gap: 24px; margin-top: 13px; margin-left: 3px; }
  .share__button { width: 30px; height: 30px; border-radius: 3px; background: var(--share-grey); }

  .contact { position: absolute; left: 822px; top: 268px; width: 378px; }
  .contact p { margin-top: 16px; margin-left: -1px; font-size: 15.5px; line-height: 21px; white-space: nowrap; }

  .contact-form { position: absolute; left: 820px; top: 400px; width: 368px; height: 370px;
    background: var(--form-bg); border-radius: 10px; box-shadow: 2px 4px 5px rgba(0,0,0,0.35); }
  .form-row { position: absolute; left: 0; display: flex; align-items: center; }
  .form-row label { width: 80px; text-align: right; font-size: 13px; padding-right: 2px; }
  .form-row input, .form-row textarea { height: 26px; width: 214px; border: 1px solid var(--field-border);
    background: var(--white); box-shadow: 2px 2px 3px rgba(0,0,0,0.3); margin-left: 4px; }
  .form-row--message { align-items: flex-start; }
  .form-row textarea { width: 270px; height: 132px; resize: none; }
  .form-actions { position: absolute; left: 78px; top: 328px; display: flex; gap: 9px; }
  .form-actions button { width: 116px; height: 23px; border: none; border-radius: 2px; background: var(--button-blue);
    color: var(--white); font-family: "Oswald", sans-serif; font-size: 8px; text-transform: uppercase; }

  .location { position: absolute; left: 824px; top: 812px; width: 376px; }
  .location p { margin-top: 14px; font-size: 17px; line-height: 21px; white-space: nowrap; }
</style>
</head>
<body>
  <header class="site-name">R.T.PELL LOGGING</header>

  <nav class="main-nav">
    <a href="#">Home</a>
    <a href="#">About Us</a>
    <a href="#">Services</a>
    <a href="#">Gallery</a>
    <a href="#">Videos</a>
  </nav>

  <section class="hero" role="img" aria-label="Sunlit pine forest with a trail through green undergrowth">
    <svg class="hero__arrow hero__arrow--prev" viewBox="0 0 60 60" aria-hidden="true">
      <circle cx="30" cy="30" r="28" fill="none" stroke="#fff" stroke-width="3"/>
      <path d="M16 30 L38 14 L32 30 L38 46 Z" fill="#fff"/>
    </svg>
    <div class="hero__label">SAMPLE IMAGE</div>
    <svg class="hero__arrow hero__arrow--next" viewBox="0 0 60 60" aria-hidden="true">
      <circle cx="30" cy="30" r="27" fill="none" stroke="#fff" stroke-width="3"/>
      <path d="M44 30 L22 14 L28 30 L22 46 Z" fill="#fff"/>
    </svg>
  </section>

  <p class="hero-caption">We are always buying timber in southeast Texas. Call for a free estimate.<br>&nbsp;If you have a timber exemption on your property, call us. We can write timber management plans for you.</p>

  <section class="welcome">
    <h2 class="section-title">Welcome!</h2>
    <p>Receive high-quality professional logging and land clearing services, from R.T. Pell Logging Company based in<br>Pine Hollow, TX. Whether your tract is large or small, our team of experts can provide the resources and<br>solutions you need to get the job done right. Our track record for consistency, timely service, and expertise will<br>continue to keep us competitive in the East Texas timber industry. We pay top dollar for your pine and hardwood timber.<br>To speak with an experienced member of staff, simply contact us 936-555-0142 at your earliest convenience.</p>
  </section>

  <aside class="share">
    <h3 class="share__title">SHARE THIS PAGE:</h3>
    <div class="share__list">
      <span class="share__button" aria-label="Share option 1"></span>
      <span class="share__button" aria-label="Share option 2"></span>
      <span class="share__button" aria-label="Share option 3"></span>
      <span class="share__button" aria-label="Share option 4"></span>
    </div>
  </aside>

  <section class="contact">
    <h2 class="section-title">Contact Us</h2>
    <p>Thank you for visiting our website.<br>Please contact us to request more information about our<br>products and services or to provide feedback about our website.</p>
  </section>

  <form class="contact-form">
    <div class="form-row" style="top:5px"><label>First Name:</label><input type="text"></div>
    <div class="form-row" style="top:42px"><label>Last Name:</label><input type="text"></div>
    <div class="form-row" style="top:77px"><label>Email:</label><input type="text"></div>
    <div class="form-row" style="top:112px"><label style="width:84px;padding-right:0">Phone Number:</label><input type="text" style="margin-left:0"></div>
    <div class="form-row" style="top:148px"><label>Subject:</label><input type="text"></div>
    <div class="form-row form-row--message" style="top:184px"><label style="padding-top:4px">Message:</label><textarea></textarea></div>
    <div class="form-actions"><button type="button">Submit</button><button type="button">Reset</button></div>
  </form>

  <section class="location">
    <h2 class="section-title">Location</h2>
    <p>We are conveniently located near you. Visit or call us today!<br>PO Box 4821</p>
  </section>
</body>
</html>
```